Billboard design for a small town Oral Surgeon

We are getting several billboards and need a design that highlights the doctors photo, and bullet points of what he does. Our business name is extremely long, so it’s a challenge to figure out how to do this. Maybe just use our logo? Open to ideas.
The logo can be shortened as designer sees fit, meaning we can drop the tag line. Important info to include:
Doctors name is Tobin Marek
The highlighted bullet points are:
•Implants
•wisdom teeth
•Jaw Surgery
•facial trauma
The goal of this billboard is to let our community know that they have an option here in Ada, our town. Many still drive to the city a couple hours away not knowing they now have an option here at home. Having a hard time finding examples of what I have in mind, so hoping this will get us going. I want it as “non-busy” as possible, so no unnecessary lines or anything that competes with the information we are trying to get across.

Target Market(s)

Everyone in town, just trying to spread the word that we are here

Industry/Entity Type

Medical/surgical (oral surgery)

Font styles to use
Sans Serif

Colors
0094D4
00A9DD
6FCCEA
C7EBF8
E9F6FB

Requirements
Must have
• *New note** Due to location of billboard, I prefer the photo of doctor to be on the left side. Must look neat and professional. Must highlight what we do.
Nice to have
• Our colors are a blue-green with silver, against black or white, but I’m flexible on this, I don’t necessarily need the colors highlighted. I’m also flexible on font style, just needs to be easy to read.
Should not have
• Distracting graphics, should not look like a dental office. That’s an issue we have is people thinking we are another dental office, we do not do any general dentistry, it’s surgery only.

```html
<!DOCTYPE html>
<html lang="en">
<head>
<meta charset="utf-8">
<title>Oral Surgeon Billboard</title>
<link rel="stylesheet" href="https://fonts.googleapis.com/css2?family=Poppins:wght@300;400;700;800&display=swap">
<style>
  :root {
    --forest: #24574e;
    --forest-text: #245a50;
    --mint: #b6e0dc;
    --white: #ffffff;
    --ink: #0d0d0d;
    --stage: #eef1f1;
    --photo-dark: #2a2c2e;
    --photo-mid: #4a4d50;
  }
  * { box-sizing: border-box; margin: 0; padding: 0; }
  html, body { width: 1200px; height: 1200px; overflow: hidden; }
  body {
    background: var(--stage);
    font-family: "Poppins", sans-serif;
    position: relative;
  }
  .billboard {
    position: absolute;
    left: 0; top: 420px;
    width: 1200px; height: 360px;
    background: var(--mint);
    overflow: hidden;
  }
  .headline-band {
    position: absolute;
    left: 0; top: 0;
    width: 1200px; height: 150px;
    background: var(--forest);
  }
  .band-rule {
    position: absolute;
    left: 262px; right: 0; top: 156px;
    height: 3px;
    background: var(--forest);
  }
  .headline {
    position: absolute;
    left: 280px; right: 20px; top: 22px;
    text-align: center;
    color: var(--white);
    font-weight: 700;
    font-size: 46px;
    line-height: 52px;
    letter-spacing: 0.5px;
  }
  .doctor-card {
    position: absolute;
    left: 30px; top: 22px;
    width: 232px; height: 318px;
    border: 3px solid var(--mint);
    background: var(--forest);
    padding: 8px;
  }
  .doctor-photo {
    width: 100%; height: 100%;
    background: radial-gradient(ellipse at 50% 35%, var(--photo-mid), var(--photo-dark) 75%);
    position: relative;
  }
  .doctor-name {
    position: absolute;
    left: 0; right: 0; bottom: 14px;
    text-align: center;
    color: var(--white);
    font-weight: 700;
    font-size: 22px;
    letter-spacing: 1px;
  }
  .services {
    position: absolute;
    left: 282px; top: 176px;
    list-style: none;
  }
  .service {
    display: flex;
    align-items: center;
    gap: 8px;
    color: var(--forest-text);
    font-weight: 800;
    font-size: 37px;
    line-height: 42px;
    letter-spacing: 1px;
    text-transform: uppercase;
  }
  .service svg { width: 24px; height: 24px; flex: none; }
  .divider {
    position: absolute;
    left: 700px; top: 170px;
    height: 172px;
    border-left: 3px dotted var(--forest-text);
  }
  .contact {
    position: absolute;
    left: 728px; top: 182px;
    width: 460px;
  }
  .practice {
    display: flex;
    align-items: center;
    gap: 12px;
  }
  .practice-dot {
    width: 34px; height: 34px;
    border-radius: 50%;
    background: var(--forest);
    flex: none;
  }
  .practice-name {
    color: var(--ink);
    font-weight: 300;
    font-size: 22px;
    line-height: 26px;
    text-transform: uppercase;
  }
  .phone {
    display: flex;
    align-items: center;
    gap: 8px;
    margin-top: 14px;
    color: var(--ink);
    font-weight: 800;
    font-size: 44px;
    line-height: 50px;
  }
  .phone svg { width: 34px; height: 34px; flex: none; }
  .website {
    margin-top: 10px;
    color: var(--ink);
    font-weight: 700;
    font-size: 20px;
    letter-spacing: 2.5px;
  }
</style>
</head>
<body>
  <section class="billboard">
    <div class="headline-band"></div>
    <div class="band-rule"></div>
    <h1 class="headline">Oral Surgeon of Choice for<br>Southeastern Oklahoma</h1>

    <div class="doctor-card">
      <div class="doctor-photo" role="img" aria-label="Portrait photo of Dr. Tobin Marek in a dark suit and red tie">
        <p class="doctor-name">MAREK, TOBIN</p>
      </div>
    </div>

    <ul class="services">
      <li class="service"><svg viewBox="0 0 24 24"><circle cx="12" cy="12" r="10" fill="none" stroke="#0d0d0d" stroke-width="2.5"/><path d="M7 12.5l3.5 3.5L18 7.5" fill="none" stroke="#0d0d0d" stroke-width="3" stroke-linecap="round" stroke-linejoin="round"/></svg>Implants</li>
      <li class="service"><svg viewBox="0 0 24 24"><circle cx="12" cy="12" r="10" fill="none" stroke="#0d0d0d" stroke-width="2.5"/><path d="M7 12.5l3.5 3.5L18 7.5" fill="none" stroke="#0d0d0d" stroke-width="3" stroke-linecap="round" stroke-linejoin="round"/></svg>Jaw Surgery</li>
      <li class="service"><svg viewBox="0 0 24 24"><circle cx="12" cy="12" r="10" fill="none" stroke="#0d0d0d" stroke-width="2.5"/><path d="M7 12.5l3.5 3.5L18 7.5" fill="none" stroke="#0d0d0d" stroke-width="3" stroke-linecap="round" stroke-linejoin="round"/></svg>Wisdom Teeth</li>
      <li class="service"><svg viewBox="0 0 24 24"><circle cx="12" cy="12" r="10" fill="none" stroke="#0d0d0d" stroke-width="2.5"/><path d="M7 12.5l3.5 3.5L18 7.5" fill="none" stroke="#0d0d0d" stroke-width="3" stroke-linecap="round" stroke-linejoin="round"/></svg>Facial Trauma</li>
    </ul>

    <div class="divider"></div>

    <div class="contact">
      <div class="practice">
        <span class="practice-dot"></span>
        <p class="practice-name">Ridgeline Oral<br>&amp; Maxillofacial Surgery</p>
      </div>
      <p class="phone"><svg viewBox="0 0 24 24"><path d="M6.6 2.5l2.6 4.2-1.8 2.1c1.2 2.6 3.2 4.6 5.8 5.8l2.1-1.8 4.2 2.6-1 3.6c-.3.9-1.1 1.4-2 1.3C9.1 19.6 4.4 14.9 3.7 7.5c-.1-.9.4-1.7 1.3-2z" fill="#0d0d0d"/><path d="M14 3.5a7 7 0 0 1 6.5 6.5M14 7a3.5 3.5 0 0 1 3 3" fill="none" stroke="#0d0d0d" stroke-width="1.6" stroke-linecap="round"/></svg>(580) 555-0148</p>
      <p class="website">www.ridgelineoralsurgery.com</p>
    </div>
  </section>
</body>
</html>
```